Christmas Collection Candle Label Design

Looking to update our existing Christmas Candle Collection labels. Labels should reflect the overall feel of our brand- www.kelvabrite.ca
Want to include some color elements. Holiday colors added into design but more muted/ earthy tones not vibrant colors . Metallic elements and line art botanical illustration. Fonts should be more align to brand
Scents
Winter Lantern
Frost Berry
Amber and Fig
Belle Étoile

```html
<!DOCTYPE html>
<html lang="en">
<head>
<meta charset="utf-8">
<title>Kelvabrite Christmas Collection Labels</title>
<link rel="stylesheet" href="https://fonts.googleapis.com/css2?family=Cookie&family=Marcellus&family=Montserrat:wght@700&family=Roboto:wght@400;500&display=swap">
<style>
  :root {
    --canvas: #e9ddd6;
    --label: #fbfbfb;
    --label-shade: #f0f0f1;
    --frame: #7a7275;
    --ink: #5b5153;
    --ink-soft: #6d6567;
    --band-dark: #8a8084;
    --band-light: #c9c2c4;
    --band-text: #f7f4f4;
    --faint-leaf: rgba(190, 190, 192, 0.28);
    --pink: #e3b6c3;
    --teal: #a9d3d0;
    --butter: #ede3a8;
    --sage: #b5d2bd;
  }
  * { margin: 0; padding: 0; box-sizing: border-box; }
  html, body { width: 901px; height: 1200px; overflow: hidden; }
  body {
    background: var(--canvas);
    position: relative;
  }
  .label {
    position: absolute;
    width: 410px;
    height: 274px;
    background: linear-gradient(100deg, var(--label) 0%, var(--label-shade) 45%, var(--label) 70%, var(--label-shade) 100%);
    box-shadow: 0 4px 14px rgba(90, 70, 70, 0.12);
    overflow: hidden;
  }
  .label--tl { left: 32px; top: 310px; }
  .label--tr { left: 459px; top: 310px; }
  .label--bl { left: 32px; top: 616px; }
  .label--br { left: 459px; top: 616px; }

  .frame-outer, .frame-inner {
    position: absolute;
    border: 1px solid var(--frame);
  }
  .frame-outer { inset: 6px; }
  .frame-inner { inset: 10px; border-width: 1.5px; }

  .botanical-faint {
    position: absolute;
    left: 14px; top: 80px;
    width: 140px; height: 160px;
    background: radial-gradient(ellipse at 50% 55%, var(--faint-leaf) 0%, rgba(255,255,255,0) 70%);
  }
  .botanical-accent {
    position: absolute;
    right: 12px; top: 36px;
    width: 150px; height: 210px;
    border-radius: 40% 40% 10% 10%;
  }
  .accent-pink   { background: radial-gradient(ellipse at 50% 45%, rgba(227,182,195,0.55) 0%, rgba(227,182,195,0) 70%); }
  .accent-teal   { background: radial-gradient(ellipse at 50% 45%, rgba(169,211,208,0.6) 0%, rgba(169,211,208,0) 70%); }
  .accent-butter { background: radial-gradient(ellipse at 45% 35%, rgba(237,227,168,0.7) 0%, rgba(237,227,168,0) 70%); }
  .accent-sage   { background: radial-gradient(ellipse at 50% 45%, rgba(181,210,189,0.6) 0%, rgba(181,210,189,0) 70%); }

  .content {
    position: absolute;
    left: 0; right: 0; top: 0;
    text-align: center;
    color: var(--ink);
  }
  .brand {
    position: absolute;
    left: 0; right: 0; top: 38px;
    font-family: "Marcellus", serif;
    font-size: 15px;
    letter-spacing: 0.5px;
    color: var(--ink);
  }
  .tagline {
    position: absolute;
    left: 0; right: 0; top: 57px;
    font-family: "Montserrat", sans-serif;
    font-weight: 700;
    font-size: 5px;
    letter-spacing: 1px;
    color: var(--ink);
  }
  .scent {
    position: absolute;
    left: 0; right: 0; top: 80px;
    font-family: "Cookie", cursive;
    font-size: 44px;
    line-height: 34px;
    color: var(--ink);
  }
  .established {
    position: absolute;
    left: 0; right: 0; top: 176px;
    font-family: "Roboto", sans-serif;
    font-size: 7px;
    line-height: 10px;
    letter-spacing: 1.4px;
    color: var(--ink-soft);
  }
  .quality {
    position: absolute;
    left: 0; right: 0; top: 220px;
    font-family: "Roboto", sans-serif;
    font-weight: 500;
    font-size: 7px;
    letter-spacing: 1.2px;
    color: var(--ink-soft);
  }
  .info-bands {
    position: absolute;
    left: 0; right: 0; top: 242px;
    height: 20px;
    display: flex;
    gap: 5px;
  }
  .info-band {
    flex: 1;
    background: linear-gradient(90deg, var(--band-dark) 0%, var(--band-light) 55%, var(--band-dark) 100%);
    font-family: "Roboto", sans-serif;
    font-size: 3.6px;
    line-height: 5px;
    letter-spacing: 0.3px;
    color: var(--band-text);
    text-align: center;
    padding-top: 5px;
  }
</style>
</head>
<body>

  <section class="label label--tl">
    <div class="botanical-faint" role="img" aria-label="Faint grey line-art leafy branch"></div>
    <div class="botanical-accent accent-pink" role="img" aria-label="Line-art botanical branch with muted pink leaves and buds"></div>
    <div class="frame-outer"></div><div class="frame-inner"></div>
    <div class="content">
      <p class="brand">KELVABRITE</p>
      <p class="tagline">PURE PLANT BASED SCENTS</p>
      <h2 class="scent">Winter<br>Lantern</h2>
      <p class="established">ESTABLISHED<br>SINCE 2005</p>
      <p class="quality">QUALITY GUARANTEED</p>
    </div>
    <div class="info-bands">
      <div class="info-band">HAND POURED IN SMALL BATCHES<br>NATURAL SOY WAX AND COTTON WICK</div>
      <div class="info-band">BURN TIME OF ABOUT FORTY HOURS<br>TRIM WICK BEFORE EACH USE</div>
      <div class="info-band">NEVER LEAVE A LIT CANDLE ALONE<br>KEEP AWAY FROM PETS AND KIDS</div>
    </div>
  </section>

  <section class="label label--tr">
    <div class="botanical-faint" role="img" aria-label="Faint grey line-art lily stem"></div>
    <div class="botanical-accent accent-teal" role="img" aria-label="Line-art lily with muted teal petals"></div>
    <div class="frame-outer"></div><div class="frame-inner"></div>
    <div class="content">
      <p class="brand">KELVABRITE</p>
      <p class="tagline">PURE PLANT BASED SCENTS</p>
      <h2 class="scent">Frost<br>Berry</h2>
      <p class="established">ESTABLISHED<br>SINCE 2005</p>
      <p class="quality">QUALITY GUARANTEED</p>
    </div>
    <div class="info-bands">
      <div class="info-band">HAND POURED IN SMALL BATCHES<br>NATURAL SOY WAX AND COTTON WICK</div>
      <div class="info-band">BURN TIME OF ABOUT FORTY HOURS<br>TRIM WICK BEFORE EACH USE</div>
      <div class="info-band">NEVER LEAVE A LIT CANDLE ALONE<br>KEEP AWAY FROM PETS AND KIDS</div>
    </div>
  </section>

  <section class="label label--bl">
    <div class="botanical-faint" role="img" aria-label="Faint grey line-art flower buds"></div>
    <div class="botanical-accent accent-butter" role="img" aria-label="Line-art tulip buds with muted yellow tint"></div>
    <div class="frame-outer"></div><div class="frame-inner"></div>
    <div class="content">
      <p class="brand">KELVABRITE</p>
      <p class="tagline">PURE PLANT BASED SCENTS</p>
      <h2 class="scent">Amber<br>&amp; Fig</h2>
      <p class="established">ESTABLISHED<br>SINCE 2005</p>
      <p class="quality">QUALITY GUARANTEED</p>
    </div>
    <div class="info-bands">
      <div class="info-band">HAND POURED IN SMALL BATCHES<br>NATURAL SOY WAX AND COTTON WICK</div>
      <div class="info-band">BURN TIME OF ABOUT FORTY HOURS<br>TRIM WICK BEFORE EACH USE</div>
      <div class="info-band">NEVER LEAVE A LIT CANDLE ALONE<br>KEEP AWAY FROM PETS AND KIDS</div>
    </div>
  </section>

  <section class="label label--br">
    <div class="botanical-faint" role="img" aria-label="Faint grey line-art leafy sprig"></div>
    <div class="botanical-accent accent-sage" role="img" aria-label="Line-art leafy branch with muted sage green leaves"></div>
    <div class="frame-outer"></div><div class="frame-inner"></div>
    <div class="content">
      <p class="brand">KELVABRITE</p>
      <p class="tagline">PURE PLANT BASED SCENTS</p>
      <h2 class="scent">Belle<br>Étoile</h2>
      <p class="established">ESTABLISHED<br>SINCE 2005</p>
      <p class="quality">QUALITY GUARANTEED</p>
    </div>
    <div class="info-bands">
      <div class="info-band">HAND POURED IN SMALL BATCHES<br>NATURAL SOY WAX AND COTTON WICK</div>
      <div class="info-band">BURN TIME OF ABOUT FORTY HOURS<br>TRIM WICK BEFORE EACH USE</div>
      <div class="info-band">NEVER LEAVE A LIT CANDLE ALONE<br>KEEP AWAY FROM PETS AND KIDS</div>
    </div>
  </section>

</body>
</html>
```